Wendlow Cellars -responsive, bootstrap website design

Looking to build a responsive service website.

Logo and pictures have been provided.

PLEASE REVIEW ATTACHED DESIGN STYLE GUIDES & CLIENT CREATIVE BRIEF FOR OUR REQUIREMENT. THANK YOU AND GOOD LUCK!

```html
<!DOCTYPE html>
<html lang="en">
<head>
<meta charset="utf-8">
<title>Wendlow Cellars</title>
<link rel="stylesheet" href="https://fonts.googleapis.com/css2?family=Josefin+Sans:wght@300;400&display=swap">
<style>
:root{
  --ink:#f2efe9;
  --ink-soft:#d8d4cc;
  --night:#1a1c1c;
  --panel:rgba(20,20,20,.72);
  --price:#d9806c;
  --line:#e8e4dc;
}
*{box-sizing:border-box;margin:0;padding:0}
html,body{width:1200px;height:997px;overflow:hidden;background:var(--night)}
body{font-family:'Josefin Sans',sans-serif;font-weight:300;color:var(--ink)}
.page{position:relative;width:1200px;height:997px;overflow:hidden}
.backdrop{position:absolute;inset:0;background:
  linear-gradient(180deg,#1e2222 0%,#222824 22%,#2a3022 34%,#263020 55%,#1f2719 75%,#1a1c14 100%)}
.abs{position:absolute}
.cart{left:888px;top:14px;font-size:12.5px;line-height:22px}
.cart svg{position:absolute;left:0;top:2px}
.cart p{margin-left:25px}
.brand{left:506px;top:45px;width:188px;height:143px;display:flex;align-items:center;justify-content:center;text-align:center;font-size:30px;line-height:1.05;color:var(--ink);font-weight:300}
.social{left:882px;top:103px;display:flex;gap:7px}
.social span{width:28px;height:28px;border:3px double var(--line);display:block}
.nav{left:184px;top:234px;width:832px;height:37px;border-top:3px double var(--line);border-bottom:3px double var(--line);font-size:16px}
.nav a{position:absolute;top:11px;color:var(--ink);text-decoration:none;white-space:nowrap}
.hero{left:184px;top:316px;width:547px;height:340px;background:
  linear-gradient(180deg,#5a6c78 0%,#9a6a78 18%,#6c6a60 38%,#3f5a2c 55%,#2f4a1e 78%,#4a4630 100%)}
.frame{border:3px double var(--line);text-align:center;color:var(--ink);font-weight:300}
.hero .frame{position:absolute;left:135px;top:137px;width:277px;height:66px;font-size:20px;line-height:22px;padding-top:11px}
.featured{left:754px;top:316px;width:262px;height:340px;background:var(--panel);text-align:center}
.featured h2{font-weight:300;font-size:15px;margin-top:20px}
.product-shot{position:absolute;left:0;top:48px;width:262px;height:130px;background:linear-gradient(180deg,#2d211c,#3a2620 40%,#221a16)}
.bottle{position:absolute;left:103px;top:6px;width:55px;height:138px;border-radius:12px 12px 4px 4px;background:linear-gradient(90deg,#111,#3a3a3a 45%,#0d0d0d)}
.arrow{position:absolute;top:116px}
.featured .desc{position:absolute;top:214px;left:8px;right:8px;font-size:10.5px;line-height:18px;color:var(--ink-soft)}
.featured .price{position:absolute;top:256px;left:0;right:0;font-size:14px;color:var(--price)}
.featured .frame{position:absolute;left:75px;top:286px;width:112px;height:37px;font-size:15px;line-height:35px}
.tile{top:701px;width:262px;height:180px}
.tile .frame{position:absolute;top:77px;left:50%;transform:translateX(-50%);height:41px;font-size:18px;line-height:39px;padding:0 16px;white-space:nowrap}
.t1{left:184px;background:linear-gradient(180deg,#6a5a44 0%,#7a6030 40%,#4e5224 70%,#30361a 100%)}
.t2{left:469px;background:linear-gradient(135deg,#3a2818,#5a3a20 40%,#2a1c12 70%,#463020)}
.t3{left:754px;background:linear-gradient(135deg,#6a5a44,#8a7454 45%,#5a4a36 80%,#3e3326)}
.deco-bottle{left:1036px;top:657px;width:148px;height:340px;border-radius:30px 30px 0 0;background:linear-gradient(90deg,#0c0c0c,#2a2a2a 45%,#0a0a0a)}
.footer{left:184px;top:932px;width:832px;border-top:3px double var(--line);font-size:11px}
.footer p{position:absolute;white-space:nowrap}
.contact svg{position:absolute;left:-22px;top:-1px}
</style>
</head>
<body>
<div class="page">
  <div class="backdrop" role="img" aria-label="Dusky vineyard landscape photograph filling the page background"></div>

  <div class="abs cart">
    <svg width="14" height="13" viewBox="0 0 14 13" fill="none" stroke="#f2efe9" stroke-width="1.4"><path d="M1 1h2l1.6 7h7L13 3H4"/><circle cx="5.5" cy="11" r="1" fill="#f2efe9"/><circle cx="10.5" cy="11" r="1" fill="#f2efe9"/></svg>
    <p>0 Product(s) - $0,00</p>
    <p>Checkout</p>
  </div>

  <div class="abs brand">Wendlow<br>Cellars</div>

  <div class="abs social" aria-label="Social links"><span></span><span></span><span></span><span></span></div>

  <nav class="abs nav">
    <a style="left:0">Home</a>
    <a style="left:106px">Story</a>
    <a style="left:210px">Wine</a>
    <a style="left:315px">Online Shop</a>
    <a style="left:463px">News</a>
    <a style="left:569px">Contact</a>
    <a style="right:0">Join The Wendlow Family</a>
  </nav>

  <section class="abs hero" role="img" aria-label="Vineyard rows under a pink sunset sky">
    <div class="frame">Welcome to Wendlow Cellars<br>- Halden Ridge Valley -</div>
  </section>

  <aside class="abs featured">
    <h2>Featured Products</h2>
    <div class="product-shot">
      <div class="bottle" role="img" aria-label="Bottle of red wine"></div>
      <svg class="arrow" style="left:68px" width="12" height="20" viewBox="0 0 12 20" fill="none" stroke="#f2efe9" stroke-width="1.5"><path d="M10 1 2 10l8 9"/></svg>
      <svg class="arrow" style="left:182px" width="12" height="20" viewBox="0 0 12 20" fill="none" stroke="#f2efe9" stroke-width="1.5"><path d="M2 1l8 9-8 9"/></svg>
    </div>
    <p class="desc">Duis scelerisque lacus vehicula odio accumsan, vitae iaculis felis sodales</p>
    <p class="price">$49,99</p>
    <div class="frame">Add to Cart</div>
  </aside>

  <a class="abs tile t1" role="img" aria-label="Vineyard valley at golden hour"><span class="frame">Vineyards</span></a>
  <a class="abs tile t2" role="img" aria-label="Racked wine bottles in a cellar"><span class="frame">Shop Wines</span></a>
  <a class="abs tile t3" role="img" aria-label="Pile of wine corks"><span class="frame">Join Us</span></a>

  <div class="abs deco-bottle" role="img" aria-label="Large dark wine bottle"></div>

  <footer class="abs footer">
    <p style="left:0;top:19px">©2014 Wendlow Cellars - All Rights Reserved.</p>
    <p style="left:337px;top:19px">Halden Ridge Valley, Oregon</p>
    <p class="contact" style="left:709px;top:19px">
      <svg width="12" height="12" viewBox="0 0 12 12" fill="#f2efe9"><path d="M2.5 0.5 4.5 3 3.3 4.4c.8 1.7 2.2 3.1 3.9 3.9L8.6 7l2.5 2-1 2C5 11 .5 6.5 .5 1.5z"/></svg>(555) 014 - 2290</p>
    <p class="contact" style="left:710px;top:41px">
      <svg width="11" height="9" viewBox="0 0 11 9" fill="none" stroke="#f2efe9" stroke-width="1.2"><rect x=".6" y=".6" width="9.8" height="7.8"/><path d="M.6.6 5.5 5 10.4.6"/></svg>contact@wendlowcellars.com</p>
  </footer>
</div>
</body>
</html>
```